Book Cover for Memoir: Sexual Assault and Traumatic Stress

I need a cover design for a memoir that is a victim's story of a sexual assault. I will need a print-on-demand cover, an eBook cover, and a 3D thumbnail image. The thumbnail and eBook cover will be used immediately, and the POD cover will be used in a few months with the full manuscript is ready. Therefore, I need an artist who is willing to make small adjustments if needed once the page count is set.

I have a image I have purchased that should give you an idea of the desired direction, but you can feel free to use your own images. I have attached some examples of book covers I like. I attached a color palette for fonts.

Overall Look: Fonts should be feminine and thin, but large to stand out. Look should be simple and elegant, and display and overall depressing feeling. There should be enough detail though to make it look professionally put together. Not TOO minimalistic.

I have also attached the Print Harbor templates if you choose to use those. If not, ensure there is an open place for the barcode on the bottom right.

Requirements
Must have
• Title: Beneath Quiet Rain
Subtitle: One Woman's Account of Fear, Guilt & Silence
Author: Dana Ruth Whitford
Audience: Mostly women 18-30
Quote (for the back): "I always thought I'd know how I'd react if I ever was raped. I was wrong. I've been wrong a lot lately."
Summary (back cover): When twenty-seven-year-old Dana Whitford wakes up with a gut-wrenching feeling, she has little memory of the horrifying events that occurred the night before. Days earlier, Dana was a spirited single mom who had abandoned her hometown to raise her daughter in the city and pursue her dreams. In the short months since Dana’s move to Seattle, she became the adored lover of a charismatic lawyer, started a new business, and finally felt life was going her way. So what happened to cause her to break?

In a gripping and heartbreaking narrative, Dana tells the true story of how her life unraveled from the traumatic events that took place that night and why what seems obvious to everyone else is impossible for Dana to believe. Beneath Quiet Rain is a chilling exploration of memory through trauma, trust in humanity, and a captivating story of strength and survival that appeals to the heart of fathers and mothers, sons and daughters, and men and women alike.
Nice to have
• BACK COVER: I'd like to have a photo on the back. This should depict the happy life of the main character before the sexual assault, and should be with her daughter. Or should be a nature scene that starts at the corner and blends into the rest of the cover. I have attached a possible image or you can use something you like.

```html
<!DOCTYPE html>
<html lang="en">
<head>
<meta charset="utf-8">
<title>Beneath Quiet Rain — Cover Spread</title>
<link rel="stylesheet" href="https://fonts.googleapis.com/css2?family=Cinzel:wght@400&family=Marcellus&family=Arimo:wght@700&family=Tinos:wght@400;700&display=swap">
<style>
  :root {
    --page: #ffffff;
    --back-black: #000000;
    --ink-white: #ffffff;
    --title-teal: #12807c;
    --ink-dark: #1b1b1b;
    --subtitle-ink: #2a2623;
    --barcode-ink: #3a2f28;
    --photo-light: #f4ece6;
    --photo-skin: #efd9cc;
    --photo-water: #7f8c98;
    --photo-deep: #3d4550;
  }
  * { margin: 0; padding: 0; box-sizing: border-box; }
  html, body {
    width: 1200px; height: 1000px; overflow: hidden;
    background: var(--page);
  }
  .canvas { position: relative; width: 1200px; height: 1000px; background: var(--page); }

  .back-cover {
    position: absolute; left: 55px; top: 115px;
    width: 577px; height: 770px;
    background: var(--back-black);
  }
  .back-copy {
    position: absolute; left: 37px; top: 36px; width: 434px;
  }
  .back-summary {
    font-family: "Arimo", Arial, sans-serif; font-weight: 700;
    font-size: 11px; line-height: 16.4px; letter-spacing: -0.05px;
    color: var(--ink-white); text-align: justify;
  }
  .back-summary p + p { margin-top: 16px; }
  .back-quote {
    margin-top: 18px; width: 440px;
    font-family: "Tinos", "Times New Roman", serif; font-weight: 700;
    font-size: 16.5px; line-height: 26px; color: var(--ink-white);
  }
  .barcode-area {
    position: absolute; left: 322px; top: 637px;
    width: 168px; height: 103px; background: var(--ink-white);
    display: flex; align-items: center; justify-content: center;
    font-family: "Tinos", "Times New Roman", serif; font-weight: 700;
    font-size: 22px; color: var(--barcode-ink);
  }

  .spine-text {
    position: absolute; left: 608px; top: 150px;
    transform-origin: 0 0; transform: rotate(90deg);
    display: flex; align-items: baseline; white-space: nowrap;
    color: var(--ink-white); width: 710px;
  }
  .spine-title { font-family: "Cinzel", serif; font-size: 31px; letter-spacing: 0.5px; }
  .spine-subtitle {
    font-family: "Tinos", "Times New Roman", serif; font-size: 12.5px;
    line-height: 13px; margin-left: 10px; white-space: normal; width: 150px;
    align-self: center;
  }
  .spine-author {
    font-family: "Marcellus", serif; font-size: 22px; margin-left: auto; letter-spacing: 0.5px;
  }

  .front-cover {
    position: absolute; left: 632px; top: 115px;
    width: 513px; height: 770px; overflow: hidden;
  }
  .cover-photo { position: absolute; inset: 0; width: 100%; height: 100%; }
  .front-subtitle {
    position: absolute; left: 46px; top: 392px;
    font-family: "Tinos", "Times New Roman", serif; font-size: 21.5px;
    line-height: 26px; color: var(--subtitle-ink);
  }
  .front-title {
    position: absolute; left: 42px; top: 455px;
    font-family: "Cinzel", serif; font-weight: 400;
    font-size: 78px; line-height: 65px; color: var(--title-teal);
    letter-spacing: -1px;
  }
  .front-author {
    position: absolute; left: 42px; top: 715px;
    font-family: "Marcellus", serif; font-size: 31px; color: var(--ink-dark);
    letter-spacing: 0.3px;
  }
</style>
</head>
<body>
<div class="canvas">

  <section class="back-cover">
    <div class="back-copy">
      <div class="back-summary">
        <p>When twenty-seven-year-old Dana Whitford wakes up with a gut-wrenching feeling, she has little memory of the horrifying events that occurred the night before. Days earlier, Dana was a spirited single mom who had abandoned her hometown to raise her daughter in the city and pursue her dreams. In the short months since Dana’s move to Seattle, she became the adored lover of a charismatic lawyer, started a new business, and finally felt life was going her way. So what happened to cause her to break?</p>
        <p>In a gripping and heartbreaking narrative, Dana tells the true story of how her life unraveled from the traumatic events that took place that night and why what seems obvious to everyone else is impossible for Dana to believe. Beneath Quiet Rain is a chilling exploration of memory through trauma, trust in humanity, and a captivating story of strength and survival that appeals to the heart of fathers and mothers, sons and daughters, and men and women alike.</p>
      </div>
      <blockquote class="back-quote">"I always thought I'd know how I'd react if I ever was raped.<br>I was wrong. I've been wrong a lot lately."</blockquote>
    </div>
    <div class="barcode-area">Bar Code</div>
  </section>

  <div class="spine-text">
    <span class="spine-title">BENEATH QUIET RAIN</span>
    <span class="spine-subtitle">One Woman's Account of Fear, Guilt &amp; Silence</span>
    <span class="spine-author">DANA RUTH WHITFORD</span>
  </div>

  <section class="front-cover">
    <svg class="cover-photo" viewBox="0 0 513 770" preserveAspectRatio="none" role="img" aria-label="Cover photograph: a young woman with dark hair lying in pale, rippling water">
      <defs>
        <linearGradient id="waterBase" x1="0" y1="0" x2="1" y2="1">
          <stop offset="0" stop-color="var(--photo-water)"/>
          <stop offset="0.35" stop-color="var(--photo-skin)"/>
          <stop offset="0.7" stop-color="var(--photo-light)"/>
          <stop offset="1" stop-color="var(--photo-light)"/>
        </linearGradient>
        <radialGradient id="hairShade" cx="0.95" cy="0.3" r="0.45">
          <stop offset="0" stop-color="var(--photo-deep)" stop-opacity="0.85"/>
          <stop offset="1" stop-color="var(--photo-deep)" stop-opacity="0"/>
        </radialGradient>
        <radialGradient id="topShade" cx="0.15" cy="0" r="0.5">
          <stop offset="0" stop-color="var(--photo-water)" stop-opacity="0.9"/>
          <stop offset="1" stop-color="var(--photo-water)" stop-opacity="0"/>
        </radialGradient>
      </defs>
      <rect width="513" height="770" fill="url(#waterBase)"/>
      <rect width="513" height="770" fill="url(#topShade)"/>
      <rect width="513" height="770" fill="url(#hairShade)"/>
    </svg>
    <p class="front-subtitle">One Woman's Account of<br>Fear, Guilt &amp; Silence</p>
    <h1 class="front-title">BENEATH<br>QUIET<br>RAIN</h1>
    <p class="front-author">DANA RUTH WHITFORD</p>
  </section>

</div>
</body>
</html>
```